Mobile Marketing Business needs a UNIQUE web design that makes users stop, adore and engage!

Unique web design for a new division of our company. Based in Los Angeles, TornaCell is a mobile marketing company offering mobile optimized websites, sms marketing, strategic and analytic consultation services. We are a b2b model targeting a wide range of industries and business sizes. Our parent company is Harbrook Digital. Tornacell needs to reflect a progressive nature, confidence, and experience - yet affordable to any business that wants to reach the mobile consumer. We want to avoid a dark website or one that is too bland. The colors should be strong, yet not overly so.

Layout should be clean, focused, - avoiding a cluttered home page. Visitors should recognize WE ARE mobile marketing - it should resonate that WE differ from competitors - Site design should resonate our brand! We've noticed competitors sites start to look and feel like the same - where the visitor may quickly exit from the home page or first inner page. There are some sites that differ which we've listed below.

The audience will range from sophisticated marketers to a local business operator who is not web savvy. The site should welcome all - not intimidate some while wowing others. We understand it's difficult for websites to be a "one size fits all" - but in reviewing competitive sites, it's apparent no one site really leaves any key impression. We'd like Tornacell to be the one.

The site should invite user to engage with the site and compel them to contact us for a demo for a better understanding of how mobiele marketing is the ultimate one 2 one sales channel that can help them improve gross sales.

Site should not be "dark" which requires using white font - we do not want "wild" or "fluorescent" colors. A tasteful, classic balance of colors that provides a comfortable experience to engage.

We realize this challenge seems .. well extremely challenging but we're quite confident there is a "design ninja" lurking out there. Are YOU the one?

Happy to provide more details and info as needed.

Sample sites that we like and feel are unique to the industry and also a site that we feel is quite basic:

www.pelvarstudio.com - clever use of banner area and using a slider to present services. However, labeling the sliders as such is a little difficult to read.

www.brantiqo.ca - clean, classic, minimalistic. Perhaps too minimal for our need but we like it. Nice use of the varying sizes and treatment of 3 promo boxes under main banner. Inner page layout is nice.

www.quarvelo.com - clever, unique. Love the call to action box (adjacent to phone) offering 3 options for next steps. Inner pages are well designed - overall site is clean, easy to read and merchandises offerings effectively.

www.brightmarshgroup.com - clean, well merchandised but home page is a bit too cluttered. good use of colors, inner page layout is simple but effective.

www.delvapost.com - clean, simple easy to follow.

www.trimesk.com - pretty basic site - in fact, you could probably replace the logo with another marketing company, etc. and the site would most likely work. We would prefer to avoid this stigma for TornaCell!!

NOTE: our logo uses a bright green that may limit it's use for mostly accents, etc. We like the contrast of colors used on www.zelnavor.com and www.paddockreel.com.au/ using the dark gray background and other colors to bring some life.

If you google "mobile marketing company", "mobile marketing services", "text messaging services", etc.. you'll notice 2 distinctive categories: amazing - like what the heck were they thinking.. and yawn - like here's another one that looks like the other..
Updates

Thank you everyone for the submissions - while they are nice, I have to say they fall into the category we were hoping to avoid (yawn, this one looks like all the other company sites)..  

Please do review the brief thoroughly - we're available if you need a specific issue addressed.  

We're still hoping a design ninja surfaces and provides a comp that makes us go "WOW'..  

cheers and good luck!

Thanks for your participation -  please stay tuned for an update to the brief along with some copy to populate the home page.  

Also... keep an eye on the project award..  we'll be increasing it after posting updates!

cheers.

UPDATE!  We have INCREASED the award in hopes of inspiring you great designers to entice your imagination and creative genetics!

PLEASE feel free to ask for further clarification or even if you want to run something by before submitting a design.  

We also have several other projects and would certainly consider those designers that truly impressed us.

As promised we're adding a bit more detail to this project.  The project requires a home and inner page layout but would like to start with the home page first.   We would also like to have a blog that differs a bit but retain some core elements of the site design.

This is a new design - our desire is to launch a website bearing an effective yet distinctive look.  Again, if you google "mobile marketing services", "mobile marketing company/companies", "mobile ..." aside from the logo varying most of the sites look the same.    We want something different..

The following may be repetitive from our brief but here goes:

Banner will focus on 3 categories - SMS/Text Marketing, Mobile Websites and Mobile Marketing:  
#1)  Headline - Did you notice how many consumers are on smartphones today?  Reach them now. 
Sub text - Mobile coupons get 10 times the redemption rate of traditional coupons
Text messages are read by 94% of recipients within 4 minutes
50% of SMS users are aged 35+ 

#2) Headline - Every day 53% of Americans use their smartphone to search the web.  Do you have a mobile optimized website?   You could be missing all these consumers each day. 
Sub text - 95% of smarthphone users search for local information 
                         70% of all mobile searches result in action within 1 hour
#3) Headline - Break through the clutter - innovative marketing campaigns distinguish your brand
Sub text - Integrate social and mobile campaigns whenever and wherever
 91% of U.S. population have a mobile device within reach 24/7

** We are open to suggestions for images or style of banner - 

Below the banner would like to have a content section featuring rotating messages titled as:
  
DID YOU KNOW? }   There are 5 times as many texters as there are Chatterly users?   < note 3-4 messages will scroll - a read more text link to an inner page for more of these facts.. 

Need 3 content sections - would prefer atypical format - not boxes, or framed areas but something different - titled:
What is a mobile website?  
Connect with mobile consumers
Mobile marketing revolution

Need:  
** a login icon for clients to access; contact us, email and text message optin - (see reference to Wendrop and Quarvelo sites from prior brief - wendrop uses creative fonts for the contact us box and email /sms optin,  quarvelo uses a creative call to action adjacent to the mobile phone with 3 options)

** to see active/ mouse over effect for navigation
** avoid a really long page - perhaps using scripts to reveal drop down boxes in content sections if necessary. 
** use of complimentary colors - keeping to white with elements of just black and green from logo gets boring
**  interesting yet not distracting shapes
** need to avoid bubble gum or flouorescent colors - note wendrop mixes colors in the main banner area in an interesting fashion. 

** need frameless design  

Again, reference the sites we liked .. and didn't like on the original brief.  Additionally we also like these sites:

1) kelbrix.com - open, expansive area - uncluttered,

2) http://presskit.daltonherald.com - love the layout and use of the black to emulate ink against white paper tying into the newspaper / brand.  We LOVE LOVE LOVE.. that sort of creativity.. in fact this is perhaps one of our favorite sites and how efficient and unique content sections, buttons, navigation, etc. is 

Looking forward to your submissions - cheers!!   

Reason: Attention all designers - this is the final extension! There are some great comps rolling in so PLEASE get your designs in soon !!!

Target Market(s)

Quite diverse actually - from local businesses (e.g., trades, professional services, retail, restaurant, hospitality, etc.) to agencies.

Industry/Entity Type

Progressive

Requirements
Must have
• Main banner of sort for messaging - would like to present 4-5 key messages that rotate/ fade on topics of SMS, mobile users, etc.
We were wondering if using mobile devices as pelvarstudio.com did to feature messages - but perhaps this limits amount of text. Also like the www.wendrop.com site with the banner rotating but also revealing portions of the slide before and after.

3-4 sections to promote key content that link to inner pages. These will feature some text - e.g., see www.brantiqo.ca - creative use of staggering box height and using script to reveal.

Main navigation = Home, Why Mobile, What We Do, Services, News (a blog), Contact. There will be 3-8 subpages for Why mobile, what we do, and services.

Footer - should contain email / text messaging sign up - see www.wendrop.com for their optin in design.

Get in Touch- again, love how www.wendrop.com has designed the "Get in Touch" call to action - not the typical button shape.

Blog - absolutely

Social icons - chatterly , workvine, and..?
Nice to have
• Not sure what we'd need here - unless you have an idea. We're open to suggestions despite our strong opinions stated so far..
Should not have
• Avoid:
anything too extreme -
avoid cartoon type illustrations
heavy use of icons
extreme colors
font that is hard to read..

```html
<!DOCTYPE html>
<html lang="en">
<head>
<meta charset="utf-8">
<title>Tornacell — Mobile Marketing</title>
<link rel="stylesheet" href="https://fonts.googleapis.com/css2?family=Source+Sans+3:wght@400;600;700&family=Arimo:wght@400;700&family=Tinos&display=swap">
<style>
:root{
  --teal-deep:#135a5f;
  --teal:#1e6f74;
  --teal-light:#3a9a9c;
  --ink:#1b1b1b;
  --white:#ffffff;
  --panel:#f1f1f1;
  --band:#dadada;
  --heading-grey:#5a5a5a;
  --body-grey:#222;
  --orange:#e8820c;
  --green:#5cb531;
  --footer-top:#0b1719;
  --footer-bottom:#215256;
  --nav-text:#3d3d3d;
}
*{box-sizing:border-box;margin:0;padding:0}
html,body{width:1200px;height:1190px;overflow:hidden}
body{
  position:relative;
  font-family:"Source Sans 3",Arial,sans-serif;
  background:radial-gradient(ellipse 700px 520px at 760px 230px,var(--teal-light),var(--teal) 55%,var(--teal-deep) 100%);
  color:var(--white);
}
.abs{position:absolute}

/* header */
.brand{left:120px;top:40px}
.brand-name{font-size:60px;font-weight:700;letter-spacing:-1px;line-height:1;display:flex;align-items:center;gap:8px}
.brand-dot{width:14px;height:14px;border-radius:50%;background:var(--white)}
.brand-tagline{font-size:17px;font-weight:600;letter-spacing:1px;margin-top:4px;padding-left:10px}
.social{top:16px;font-size:22px;font-weight:700;letter-spacing:.5px}
.social-chatterly{left:757px}
.social-chirpwave{left:868px}
.client-btn{left:992px;top:12px;width:118px;height:38px;border-radius:5px;background:linear-gradient(#fff,#dcdcdc);color:var(--nav-text);font-size:14px;font-weight:700;display:flex;align-items:center;justify-content:center;gap:8px;box-shadow:0 1px 3px rgba(0,0,0,.3)}
.main-nav{left:468px;top:65px;width:642px;height:45px;background:linear-gradient(#fff,#e2e2e2);border-radius:4px;display:flex;box-shadow:0 2px 4px rgba(0,0,0,.25)}
.main-nav a{color:var(--nav-text);text-decoration:none;font-size:14px;font-weight:700;display:flex;align-items:center;justify-content:center;border-right:1px solid #c8c8c8}
.main-nav a:last-child{border-right:0}
.main-nav a:hover{background:#d4eaea}
.nav-home{width:42px}.nav-why{width:140px}.nav-what{width:136px}.nav-services{width:113px}.nav-news{width:90px}.nav-contact{width:121px}

/* hero */
.hero-copy{left:118px;top:158px;width:500px}
.hero-headline{font-size:31px;font-weight:700;line-height:1.02;letter-spacing:-.5px;margin-bottom:12px}
.hero-fact{font-size:24px;line-height:1.18;margin-bottom:12px}
.slider-dots{left:122px;top:471px;display:flex;gap:6px}
.slider-dots span{width:17px;height:17px;border-radius:50%;border:2px solid var(--white)}
.hero-photo{left:550px;top:115px;width:460px;height:393px;background:radial-gradient(ellipse at 50% 45%,#d9e6ee 0%,#9fb7c7 45%,rgba(58,154,156,0) 75%)}
.get-in-touch{left:984px;top:412px;width:136px;height:136px;border-radius:50%;background:radial-gradient(circle at 40% 35%,#3a3a3a,#111);border:3px solid #555;color:var(--white);display:flex;flex-direction:column;align-items:center;justify-content:center;line-height:.9;font-size:36px;font-weight:700;transform:rotate(-6deg);z-index:3}
.get-in-touch em{font-style:normal;color:var(--orange)}

/* content panel */
.content-panel{left:96px;top:508px;width:1014px;height:444px;background:var(--panel)}
.did-you-know{left:120px;top:530px;width:952px;height:118px;background:var(--band);border-radius:6px;color:var(--ink)}
.dyk-title{position:absolute;left:56px;top:15px;font-family:"Tinos",serif;font-size:42px;line-height:1.03;color:var(--orange);text-align:center}
.dyk-brace{position:absolute;left:254px;top:10px;font-family:"Tinos",serif;font-size:86px;color:#9c9c9c;line-height:1}
.dyk-text{position:absolute;left:312px;top:27px;font-family:"Tinos",serif;font-size:27px;line-height:1.2;text-align:center;width:360px}
.dyk-btn{position:absolute;left:746px;top:28px;width:170px;height:63px;background:linear-gradient(#fff,#e4e4e4);border-radius:5px;box-shadow:0 1px 3px rgba(0,0,0,.3);font-family:"Arimo",sans-serif;font-size:15px;font-weight:700;color:var(--nav-text);text-align:center;display:flex;align-items:center;justify-content:center;line-height:1.2}

.feature{width:300px;text-align:center;color:var(--body-grey);top:672px}
.feature-1{left:445px;margin-left:-320px}
.feature-2{left:450px}
.feature-3{left:776px}
.feature svg{height:58px;display:block;margin:0 auto 14px}
.feature h2{font-family:"Arimo",sans-serif;font-size:24px;color:var(--heading-grey);line-height:1.05;margin-bottom:20px}
.feature p{font-family:"Arimo",sans-serif;font-size:13px;line-height:1.3;text-align:left;margin-bottom:22px}
.read-more{display:inline-flex;align-items:center;gap:8px;width:116px;height:36px;justify-content:center;background:linear-gradient(#fff,#e6e6e6);border-radius:3px;box-shadow:0 1px 3px rgba(0,0,0,.3);color:#8b9a2e;font-size:15px}

/* footer */
.footer-band{left:96px;top:952px;width:1014px;height:156px;background:linear-gradient(var(--footer-top),var(--footer-bottom))}
.footer-email{left:118px;top:998px;width:305px;height:60px;background:#1c2628;border:1px solid #3c4a4c;border-radius:3px;display:flex;align-items:center;justify-content:center;font-size:25px;font-weight:600}
.optin-label{font-size:15px;font-weight:700}
.optin-input{height:33px;background:var(--white);border-radius:2px;color:#444;font-size:13px;padding-left:10px;display:flex;align-items:center}
.optin-submit{height:31px;width:56px;background:var(--green);border-radius:2px;font-size:12px;display:flex;align-items:center;justify-content:center}
.bottom-links{top:1128px;font-size:11px;left:114px;width:990px;display:flex;justify-content:space-between}
.bottom-links b{font-weight:700}
</style>
</head>
<body>

<header>
  <div class="abs brand">
    <div class="brand-name"><span class="brand-dot"></span>tornacell</div>
    <div class="brand-tagline">MAKE YOUR BRAND TORNA.CELL</div>
  </div>
  <div class="abs social social-chatterly">chatterly</div>
  <div class="abs social social-chirpwave">Chirpwave</div>
  <div class="abs client-btn">
    <svg width="26" height="16" viewBox="0 0 26 16"><circle cx="7" cy="5" r="3.5" fill="#666"/><circle cx="19" cy="5" r="3.5" fill="#666"/><circle cx="13" cy="4" r="4" fill="#555"/><path d="M4 16c0-5 4-7 9-7s9 2 9 7z" fill="#555"/></svg>CLIENT
  </div>
  <nav class="abs main-nav">
    <a class="nav-home" href="#"><svg width="16" height="15" viewBox="0 0 16 15"><path d="M8 0L0 7h2v8h4v-5h4v5h4V7h2z" fill="#3d3d3d"/></svg></a>
    <a class="nav-why" href="#">WHY MOBILE</a>
    <a class="nav-what" href="#">WHAT WE DO</a>
    <a class="nav-services" href="#">SERVICES</a>
    <a class="nav-news" href="#">NEWS</a>
    <a class="nav-contact" href="#">CONTACT</a>
  </nav>
</header>

<section>
  <div class="abs hero-photo" role="img" aria-label="Businessman holding a tablet in front of his face, with floating photos of mobile users"></div>
  <div class="abs hero-copy">
    <h1 class="hero-headline">Did you notice how many consumers are on smartphones today?<br>Reach them now.</h1>
    <p class="hero-fact">Mobile coupons get 10 times the redemption rate of traditional coupons.</p>
    <p class="hero-fact">Text messages are read by 94% of recipients within 4 minutes 50% of SMS users are aged 35+ .</p>
  </div>
  <div class="abs slider-dots">
    <span style="background:#8a9a2a"></span><span style="background:#5a1a3a"></span><span style="background:#b0234a"></span><span style="background:#e07a10"></span><span style="background:transparent"></span>
  </div>
  <div class="abs get-in-touch"><span>get in</span><em>touch</em></div>
</section>

<main>
  <div class="abs content-panel"></div>
  <div class="abs did-you-know">
    <div class="dyk-title">DID YOU<br>KNOW?</div>
    <div class="dyk-brace">}</div>
    <div class="dyk-text">There are 5 times as many texters as there are Chatterly users?</div>
    <div class="dyk-btn">GET MORE<br>MOBILE FAQ</div>
  </div>

  <article class="abs feature feature-1">
    <svg viewBox="0 0 30 50" width="35"><rect x="2" y="2" width="26" height="46" rx="4" fill="none" stroke="#9a9a9a" stroke-width="3"/><rect x="6" y="8" width="18" height="30" fill="#c4c4c4"/><circle cx="15" cy="43" r="2" fill="#9a9a9a"/></svg>
    <h2>What is a Mobile<br>Website?</h2>
    <p>Lorem ipsum dolor sit amet, consecteturadipi sicing elit, sed do eiusmod tempor incididunt Lorem ipsum dolor sit amet, consecteturadipi</p>
    <span class="read-more">Read More <svg width="8" height="12" viewBox="0 0 8 12"><path d="M1 1l5 5-5 5" stroke="#999" stroke-width="1.5" fill="none"/></svg></span>
  </article>
  <article class="abs feature feature-2">
    <svg viewBox="0 0 66 40" width="66"><circle cx="16" cy="14" r="7" fill="#a8a8a8"/><circle cx="50" cy="14" r="7" fill="#a8a8a8"/><circle cx="33" cy="11" r="9" fill="#959595"/><path d="M4 40c0-11 6-16 12-16s10 4 12 8" fill="#a8a8a8"/><path d="M62 40c0-11-6-16-12-16s-10 4-12 8" fill="#a8a8a8"/><path d="M16 40c0-12 8-18 17-18s17 6 17 18z" fill="#959595"/></svg>
    <h2>Connect With Mobile<br>Consumers</h2>
    <p>Lorem ipsum dolor sit amet, consecteturadipi sicing elit, sed do eiusmod tempor incididunt Lorem ipsum dolor sit amet, consecteturadipi</p>
    <span class="read-more">Read More <svg width="8" height="12" viewBox="0 0 8 12"><path d="M1 1l5 5-5 5" stroke="#999" stroke-width="1.5" fill="none"/></svg></span>
  </article>
  <article class="abs feature feature-3">
    <svg viewBox="0 0 50 44" width="50"><rect x="2" y="14" width="8" height="14" fill="#9a9a9a"/><path d="M12 14L40 2v38L12 28z" fill="#9a9a9a"/><rect x="14" y="28" width="8" height="14" fill="#9a9a9a"/></svg>
    <h2>Mobile Marketing<br>Revolution</h2>
    <p>Lorem ipsum dolor sit amet, consecteturadipi sicing elit, sed do eiusmod tempor incididunt Lorem ipsum dolor sit amet, consecteturadipi</p>
    <span class="read-more">Read More <svg width="8" height="12" viewBox="0 0 8 12"><path d="M1 1l5 5-5 5" stroke="#999" stroke-width="1.5" fill="none"/></svg></span>
  </article>
</main>

<footer>
  <div class="abs footer-band"></div>
  <div class="abs footer-email">info@tornacell.com</div>
  <div class="abs optin-label" style="left:445px;top:998px">Receceive Our Monthly Newsletter</div>
  <div class="abs optin-input" style="left:445px;top:1024px;width:242px">Enter Email</div>
  <div class="abs optin-submit" style="left:699px;top:1025px">submit</div>
  <div class="abs optin-label" style="left:773px;top:999px">Get Tornacell Text Alerts</div>
  <div class="abs optin-input" style="left:773px;top:1024px;width:247px">Enter Phone Number</div>
  <div class="abs optin-submit" style="left:1032px;top:1025px">submit</div>
  <div class="abs bottom-links">
    <span>Home | Why Mobile | What We Do | Services |News | Contact</span>
    <span>Copyright © Tornacell, All Rights Reserved. &nbsp;| &nbsp;Privacy Policy &nbsp;| &nbsp;SMS Terms &nbsp;| &nbsp;Accepted Use Policy &nbsp;| &nbsp;<b>sales@tornacell.com</b></span>
  </div>
</footer>

</body>
</html>
```